Stage Design Company Business Card

We are looking to step up up our business card design for our team.

We are a Full service Design and Consultation company for Stage and TV with an emphasis in Theatrical Lighting.

We like our materials to be clean and modern with solid colors free of patterns and gradients. Our brand consists of 4 primary colors Purple, Black, Grey, and White. Provided is our Word Mark as well as our Symbol Logo.

We would like our cards to leave an impression beyond the information, show our attention to design and detail, and make our marks an easily recognized feature (together or apart) for our clients.

We need a warm approachable comfortable feel for some clients, and a professional flair for the board member type clients.

Attached are our brand elements, and our existing cards to give a sense of our style and a glipse at the information we provide on our cards.

Target Market(s)

broad client base from church leaders to high school teachers and architects.

Industry/Entity Type

Business

Contact Information for Business Card

We format our phone number with periods not parenthesis or dashes. Information will be edited for each of our team members, and team member specific cards are not part of this scope, but rather a template so to speak.

Font styles to use
Sans Serif

Colors
6b449b
ffffff
000000
333333
aaaaaa

Requirements
Must have
• Wordmark and logo mark present (does not need to exist on the same side of card)
• Brand Colors,
• Name, Phone, Email, Address.
• Unique choices that make someone stop and take a second look
Nice to have
• It would be nice to somehow convey what we DO, as our brand name does not lend itself to this, outside of an obvious tagline though.....
• social media if not crowded. all of our handles match (instagram, twitter, facebook)
Should not have
• "clipart"

```html
<!DOCTYPE html>
<html lang="en">
<head>
<meta charset="utf-8">
<title>Vello Entertainment – Business Card</title>
<link href="https://fonts.googleapis.com/css2?family=Questrial&display=swap" rel="stylesheet">
<style>
  :root {
    --backdrop: #5e5e5e;
    --brand-purple: #392870;
    --card-white: #ffffff;
    --ink-grey: #5a5a5a;
    --icon-grey: #b4b6b9;
    --tag-grey: #9a96b4;
    --ink-dark: #222222;
  }
  * { margin: 0; padding: 0; box-sizing: border-box; }
  html, body {
    width: 1200px; height: 1200px; overflow: hidden;
    background: var(--backdrop);
    font-family: "Questrial", sans-serif;
  }
  .stage { position: relative; width: 1200px; height: 1200px; }
  .card {
    position: absolute; top: 259px; width: 400px; height: 682px;
  }
  .card--front { left: 178px; background: var(--card-white); }
  .card--back { left: 622px; background: var(--brand-purple); }

  .wordmark {
    position: absolute; left: 0; width: 100%;
    text-align: center; font-size: 40px; letter-spacing: 30px;
    padding-left: 30px; line-height: 1;
  }
  .card--front .wordmark { top: 120px; color: var(--brand-purple); }
  .card--back .wordmark { top: 292px; color: var(--card-white); }

  .tagline {
    position: absolute; top: 373px; left: 0; width: 100%;
    text-align: center; font-size: 10px; letter-spacing: 11px;
    padding-left: 11px; color: var(--tag-grey);
  }

  .name-block {
    position: absolute; left: 0; top: 230px;
  }
  .name-block .accent {
    position: absolute; left: 0; top: 0; width: 63px; height: 51px;
    background: var(--brand-purple);
  }
  .name-block .name {
    position: absolute; left: 81px; top: -2px; white-space: nowrap;
    font-size: 31px; color: var(--brand-purple); line-height: 1.1;
  }
  .name-block .title {
    position: absolute; left: 81px; top: 35px; white-space: nowrap;
    font-size: 17px; color: var(--ink-grey);
  }

  .contact {
    position: absolute; left: 81px; top: 342px; list-style: none;
    font-size: 19px; color: var(--ink-grey); line-height: 26px;
  }
  .contact li { display: flex; align-items: center; gap: 8px; }
  .contact svg { width: 16px; height: 16px; flex: none; }

  .address {
    position: absolute; left: 81px; top: 442px;
    font-size: 19px; color: var(--ink-grey); line-height: 26px;
    font-style: normal;
  }

  .social {
    position: absolute; left: 82px; top: 540px;
    display: flex; gap: 30px;
  }
  .social span {
    width: 54px; height: 54px; border-radius: 50%;
    background: var(--icon-grey); display: block;
  }
  .handle {
    position: absolute; left: 0; width: 100%; top: 608px;
    text-align: center; padding-left: 40px;
    font-size: 20px; color: var(--ink-dark); font-weight: 400;
  }
</style>
</head>
<body>
<main class="stage">
  <section class="card card--front" aria-label="Card front">
    <div class="wordmark">VELLO</div>

    <div class="name-block">
      <div class="accent"></div>
      <div class="name">Mark R Halden</div>
      <div class="title">JOB TITLE</div>
    </div>

    <ul class="contact">
      <li>
        <svg viewBox="0 0 16 16" fill="none" stroke="#392870" stroke-width="1.4"><path d="M4 1.5l2.5 3-1.5 1.5c.8 2 2.5 3.7 4.5 4.5L11 9l3 2.5-1.5 2.5C7 14 2 9 2 3z"/></svg>
        555.014.2290
      </li>
      <li>
        <svg viewBox="0 0 16 16" fill="none" stroke="#392870" stroke-width="1.4"><rect x="1.5" y="3.5" width="13" height="9"/><path d="M1.5 3.5L8 9l6.5-5.5"/></svg>
        mark@vello-e.com
      </li>
      <li>
        <svg viewBox="0 0 16 16" fill="none" stroke="#392870" stroke-width="1.3"><circle cx="8" cy="8" r="6.5"/><ellipse cx="8" cy="8" rx="3" ry="6.5"/><path d="M1.5 8h13M2.5 5h11M2.5 11h11"/></svg>
        www.vello-e.com
      </li>
    </ul>

    <address class="address">52 N Elm Ave<br>Tamsen, AZ 85000</address>

    <div class="social" aria-label="Social networks">
      <span></span><span></span><span></span>
    </div>
    <div class="handle">@velloentertain</div>
  </section>

  <section class="card card--back" aria-label="Card back">
    <div class="wordmark">VELLO</div>
    <div class="tagline">ENTERTAINMENT</div>
  </section>
</main>
</body>
</html>
```